Window Company website re-design

We are creating a new website design for http://harborpanes.example and we are going to be using wordpress for the site. The idea is to make it appeal to homeowners, more than half of the visitors will be female so the design must appeal to them with appropriate colors and shapes. Historically the website has been dark with a black background and the idea is to keep some of that but make it much brighter with textures and inviting colors.
Major competitors which we will mimic are the following in order of favorites:
http://www.birchvalleyglass.example/ (this is something we really like because of the full width, call to action, easy to navigate, space for
http://www.grainhillexteriors.example/ (this is a nice wide design with a lot of great image space and call to actions)
http://www.restorebyhollister.example/ (the full width is nice here)
http://www.duskpointpanes.example/ (the slide over option showing the window is nice here.)
Others:
http://www.torvane.example/
http://www.quiro.example/home/default.aspx
http://www.hollisterpanes.example/
https://www.glazeplanet.example/
http://www.delcot.example/

Harbor is the leader in the industry so they want a design that is going to portray that. The owners say that their competitors always copy what they do so this design must be cutting edge.

Important elements need to included:
1. Make the design convey very obviously they are a replacement window and door company.
2. Very clear “request a free estimate” call to action box on the homepage.
3. Area for the “Live Support” call to action
4. Navigation:

- Home
- Why Harbor
o Saves Dollars, Makes Sense
o We Have You Covered Start to Finish
o The Harbor Difference
o Pitfalls to Avoid
- Windows and Doors
o Windows
 Double Hung Windows
 Awning Windows
 Basement Hopper Windows
 Bow Windows
 Garden Windows
 Casement Windows
 Bay Windows
 Slider Windows
 Dead-Lite / Specialty / Transom
o Doors
 Storm Doors
 Harbor French Doors
 Patio Slider Doors
 Door Catalog
 Keypad Deadbolt
o Before and After
- About Us
o Testimonials
o Directions
o Warranty
o Employment
o Manufacturing process
o Home Shows
o Community Involvement
- Financing
- Commercial Division
- Careers
- Contact Us

Important elements for the Home Page:
1. Call to action – request a free quote
2. Awards
3. Live support
4. Guarantee
5. Featured testimonials
6. Press releases
7. Locations (Map?)

The attached photos can be used for the homepage images

Target Market(s)

The target market is middle income home owners who want good quality and great service.

Industry/Entity Type

Industry

Font styles to use
Sans Serif

Colors

Designer to choose colors to be used in the design.

Requirements
Must have
• We will need 2 designs, one for the homepage and the other for the inner pages.

2. Awards
3. Live support
4. Guarantee
5. Featured testimonials
6. Press releases
7. Locations (Map?)

```html
<!DOCTYPE html>
<html lang="en">
<head>
<meta charset="utf-8">
<title>Harbor – Replacement Windows &amp; Doors</title>
<link href="https://fonts.googleapis.com/css2?family=Tinos:ital,wght@0,400;0,700;1,400&display=swap" rel="stylesheet">
<style>
:root{
  --ink:#111111;
  --panel:#0d0d0d;
  --text:#2b2b2b;
  --white:#ffffff;
  --yellow:#fff200;
  --rule:#3a3a3a;
  --field-border:#c9c9c9;
}
*{box-sizing:border-box;margin:0;padding:0}
html,body{width:1200px;height:999px;overflow:hidden;background:var(--white);font-family:"Tinos","Times New Roman",serif;color:var(--text)}
.site{position:relative;width:1200px;height:999px}

.masthead{position:absolute;left:0;top:0;width:1200px;height:97px;background:var(--ink)}
.brand{position:absolute;left:133px;top:31px;display:flex;align-items:center;gap:9px}
.brand-mark{width:22px;height:22px;background:var(--white)}
.brand-name{font-size:30px;font-weight:400;line-height:32px;color:var(--white)}
.call{position:absolute;right:132px;top:10px;color:var(--white);font-size:26px;letter-spacing:.2px}
.nav-rule{position:absolute;left:294px;top:50px;width:775px;height:1px;background:#d8d8d8}
.main-nav{position:absolute;left:0;top:61px;width:1200px;height:20px;font-size:15px}
.main-nav a{position:absolute;top:0;color:var(--white);text-decoration:none;white-space:nowrap}

.hero{position:absolute;left:0;top:97px;width:1200px;height:418px;
  background:linear-gradient(90deg,#e9ebe8 0%,#cfd2cc 18%,#5c6a4e 36%,#dcdcd6 46%,#54674a 58%,#e2e2dc 66%,#4f6244 78%,#d9d9d4 90%,#bfc3bb 100%)}

.quote-box{position:absolute;left:129px;top:148px;width:301px;height:424px;background:var(--panel);padding:28px 19px 0}
.quote-title{color:var(--white);text-align:center;font-size:32px;line-height:33px;font-weight:400}
.quote-title u{text-decoration:none;border-bottom:1px solid var(--white)}
.field{display:block;width:260px;height:33px;margin-top:20px;background:var(--white);border:2px solid var(--field-border);font:italic 14px "Tinos",serif;color:#666;padding:7px 12px}
.quote-title + .field{margin-top:23px}
.field.select{position:relative;margin-top:27px}
.field.select svg{position:absolute;right:6px;top:11px}
.price-btn{display:block;margin-top:28px;width:260px;height:43px;background:var(--yellow);color:#222;text-align:center;font:italic 24px/43px "Tinos",serif}

.live-support{position:absolute;left:1157px;top:148px;width:43px;height:157px;background:var(--yellow)}
.live-support span{position:absolute;left:10px;top:118px;transform:rotate(-90deg);transform-origin:left top;font:italic 17px "Tinos",serif;color:#222;white-space:nowrap}
.live-support svg{position:absolute;left:9px;top:124px}

.guarantee{position:absolute;left:130px;top:608px;width:668px}
.section-head{display:flex;align-items:center;gap:8px;font-size:31px;font-weight:400;color:#333;padding-bottom:4px;border-bottom:1px solid var(--rule)}
.lead{font-style:italic;font-size:15px;line-height:26px;margin-top:28px;max-width:630px}
.checklist{list-style:none;display:grid;grid-template-columns:266px 300px;margin:28px 0 0 76px;row-gap:10px}
.checklist li{font-style:italic;font-size:15px;line-height:26px;position:relative;padding-left:28px}
.checklist li:nth-child(even){padding-left:46px}
.checklist li svg{position:absolute;left:0;top:6px}
.body-copy{font-style:italic;font-size:15px;line-height:26px;margin-top:26px;max-width:660px}

.testimonials{position:absolute;left:849px;top:534px;width:218px;text-align:center}
.testimonials h2{font-size:30px;font-weight:400;line-height:33px;margin-top:2px;color:#333;padding-bottom:13px;border-bottom:1px solid var(--rule)}
.t-item{margin-top:24px}
.t-place{font-style:italic;font-size:18px}
.t-video{position:relative;height:110px;margin-top:8px;background:linear-gradient(135deg,#8a8a8a,#3a3a3a 55%,#c9c9c9)}
.t-play{position:absolute;left:61px;top:103px;width:100px;height:34px;background:var(--yellow);font:italic 14px/34px "Tinos",serif;color:#222}
.t-sep{height:1px;background:var(--rule);margin-top:58px}
.t-item.second{margin-top:36px}
.t-item.second .t-video{height:70px;background:linear-gradient(180deg,#2a2a2a,#bdbdbd)}
</style>
</head>
<body>
<div class="site">
  <header class="masthead">
    <div class="brand"><span class="brand-mark"></span><span class="brand-name">Harbor</span></div>
    <div class="call">CALL NOW 1-800-555-0142</div>
    <div class="nav-rule"></div>
    <nav class="main-nav">
      <a href="#" style="left:294px">Home</a>
      <a href="#" style="left:356px">Why Harbor</a>
      <a href="#" style="left:461px">Windows &amp; Doors</a>
      <a href="#" style="left:605px">About Us</a>
      <a href="#" style="left:688px">Financing</a>
      <a href="#" style="left:775px">Commercial Division</a>
      <a href="#" style="left:932px">Careers</a>
      <a href="#" style="left:1003px">Contact Us</a>
    </nav>
  </header>

  <div class="hero" role="img" aria-label="Sunroom with tall white double hung windows looking out to a wooded backyard and deck"></div>

  <form class="quote-box">
    <h1 class="quote-title">REQUEST<br>A <u>FREE</u> QUOTE</h1>
    <div class="field">Fulll name</div>
    <div class="field">Email</div>
    <div class="field">Telephone</div>
    <div class="field select">Product interested in
      <svg width="14" height="9" viewBox="0 0 14 9"><path d="M0 0h14L7 9z" fill="#111"/></svg>
    </div>
    <a class="price-btn">Get a Price ›</a>
  </form>

  <a class="live-support" href="#">
    <span>Live Support ›</span>
    <svg width="26" height="26" viewBox="0 0 26 26" fill="none" stroke="#111" stroke-width="2"><circle cx="13" cy="13" r="11"/><circle cx="13" cy="13" r="5"/><path d="M5 5l4 4M21 5l-4 4M5 21l4-4M21 21l-4-4"/></svg>
  </a>

  <section class="guarantee">
    <h2 class="section-head">
      <svg width="34" height="34" viewBox="0 0 34 34" fill="none" stroke="#222" stroke-width="2"><circle cx="17" cy="13" r="10"/><circle cx="17" cy="13" r="6"/><path d="M10 20l-5 11 6-2 3 4 3-10M24 20l5 11-6-2-3 4-3-10"/></svg>
      GUARANTEE
    </h2>
    <p class="lead">We are so confident in our work that we offer one of the best guarantees in the industry. We cover everything 100%.</p>
    <ul class="checklist">
      <li><svg width="18" height="14" viewBox="0 0 18 14"><path d="M1 7l5 5L17 1" fill="none" stroke="#222" stroke-width="2"/></svg>Windows</li>
      <li><svg width="18" height="14" viewBox="0 0 18 14"><path d="M1 7l5 5L17 1" fill="none" stroke="#222" stroke-width="2"/></svg>Parts</li>
      <li><svg width="18" height="14" viewBox="0 0 18 14"><path d="M1 7l5 5L17 1" fill="none" stroke="#222" stroke-width="2"/></svg>Glass Breakage</li>
      <li><svg width="18" height="14" viewBox="0 0 18 14"><path d="M1 7l5 5L17 1" fill="none" stroke="#222" stroke-width="2"/></svg>Service</li>
      <li><svg width="18" height="14" viewBox="0 0 18 14"><path d="M1 7l5 5L17 1" fill="none" stroke="#222" stroke-width="2"/></svg>Seals</li>
      <li><svg width="18" height="14" viewBox="0 0 18 14"><path d="M1 7l5 5L17 1" fill="none" stroke="#222" stroke-width="2"/></svg>We even cover labor and installation.</li>
      <li><svg width="18" height="14" viewBox="0 0 18 14"><path d="M1 7l5 5L17 1" fill="none" stroke="#222" stroke-width="2"/></svg>Vinyl</li>
    </ul>
    <p class="body-copy">Are you looking for the very best replacement window money can buy? You've found it with Harbor Windows. Replacing your home's windows with high-performance Harbor Windows is one of the wisest home improvement investments you'll ever make.</p>
  </section>

  <aside class="testimonials">
    <svg width="34" height="30" viewBox="0 0 34 30" fill="none" stroke="#222" stroke-width="2"><path d="M2 2h30v19H14l-7 6v-6H2z"/><path d="M8 8h18M8 12h18M8 16h12"/></svg>
    <h2>FEATURED<br>TESTIMONIALS</h2>
    <div class="t-item">
      <div class="t-place">West Haven, CT</div>
      <div class="t-video" role="img" aria-label="Video still of homeowners talking about their new windows">
        <a class="t-play">Play Video ›</a>
      </div>
    </div>
    <div class="t-sep"></div>
    <div class="t-item second">
      <div class="t-place">Sam R, Linden Falls PA</div>
      <div class="t-video" role="img" aria-label="Video still of a customer testimonial"></div>
    </div>
  </aside>
</div>
</body>
</html>
```